certificate to present to patients after successful vasectomy

creation of a A4 sized colour certificate that can be presented to patients after their three month semen test confirms a successful vasectomy.
I have attached my current logo for Clearpath Vasectomy with the colours blue and green. I have attached a collage of example fun images related to congratulating men after their vasectomy.

Target Market(s)

A fun certificate to provide to men after a successful vasectomy. THis is a bit more playful/fun than traditional medical illustration/medical information. Men can stick it on the fridge or wave it about a family events to mortify their children.

Font styles to use
Sans Serif

Colors

Designer to choose colors to be used in the design.

Requirements
Must have
• Clearpath Vasectomy Logo and these or complimentary colours
• Be editable to add the patients name and date of certificate
Nice to have
• continuation of design themes from logo
Should not have
• should not have realistic or medical illustration of penis/scrotum. This should be a fun/silly certificate they can put on the family fridge or cork board

```html
<!DOCTYPE html>
<html lang="en">
<head>
<meta charset="utf-8">
<title>Clearpath Vasectomy – Certificate of Success</title>
<link rel="stylesheet" href="https://fonts.googleapis.com/css2?family=Cormorant+Garamond:wght@500;600&family=Roboto:wght@400;500&family=Roboto+Condensed:wght@400;700&display=swap">
<style>
  :root {
    --navy: #00295c;
    --navy-deep: #001f55;
    --navy-shadow: #00163f;
    --gold: #e3b94a;
    --gold-light: #f3d36a;
    --gold-dark: #b78227;
    --grey: #bdbdbd;
    --name-grey: #c4c4c4;
    --ink: #0c2350;
    --brand-blue: #2a7fc1;
    --web-blue: #1f5a93;
    --paper: #ffffff;
  }
  * { margin: 0; padding: 0; box-sizing: border-box; }
  html, body { width: 1200px; height: 927px; overflow: hidden; background: var(--paper); }
  .certificate { position: relative; width: 1200px; height: 927px; background: var(--paper); overflow: hidden; }
  .backdrop { position: absolute; inset: 0; }
  .title {
    position: absolute; top: 52px; left: 0; width: 100%; text-align: center;
    font-family: "Cormorant Garamond", serif; font-weight: 600; font-size: 112px;
    line-height: 1; color: var(--gold); letter-spacing: 0.005em;
  }
  .recipient {
    position: absolute; top: 438px; left: 0; width: 100%; text-align: center;
    font-family: "Roboto", sans-serif; font-weight: 400; font-size: 70px; line-height: 1;
    color: var(--name-grey); letter-spacing: 0.36em; padding-left: 0.36em;
  }
  .achievement {
    position: absolute; top: 566px; left: 0; width: 100%; text-align: center;
    font-family: "Cormorant Garamond", serif; font-weight: 500; font-size: 40px;
    line-height: 1; color: var(--ink);
  }
  .date-field { position: absolute; left: 150px; top: 712px; width: 196px; }
  .date-label {
    display: block; margin-left: 8px; font-family: "Roboto Condensed", sans-serif;
    font-weight: 700; font-size: 16px; color: var(--ink);
  }
  .date-line { margin-top: 22px; height: 2px; background: var(--ink); }
  .brand {
    position: absolute; left: 533px; top: 672px; display: flex; align-items: center; gap: 12px;
  }
  .brand-square { width: 16px; height: 16px; background: var(--brand-blue); flex: none; }
  .brand-name {
    font-family: "Roboto", sans-serif; font-weight: 500; font-size: 27px; line-height: 1.05;
    color: var(--brand-blue); text-transform: uppercase;
  }
  .signature-mark {
    position: absolute; left: 820px; top: 630px; width: 212px; height: 82px;
    background: linear-gradient(90deg, rgba(12,35,80,0.04), rgba(12,35,80,0.10), rgba(12,35,80,0.04));
    border-radius: 40px;
  }
  .signatory { position: absolute; left: 913px; top: 713px; font-family: "Roboto Condensed", sans-serif; color: var(--ink); }
  .signatory-name { font-weight: 700; font-size: 17px; line-height: 1.3; }
  .signatory-org { font-weight: 400; font-size: 17px; line-height: 1.3; }
  .website {
    position: absolute; top: 818px; left: 0; width: 100%; text-align: center;
    font-family: "Roboto", sans-serif; font-weight: 400; font-size: 20px;
    letter-spacing: 0.28em; color: var(--web-blue);
  }
  .footer-band { position: absolute; left: 0; bottom: 0; width: 100%; height: 67px; background: var(--navy-deep); }
</style>
</head>
<body>
<main class="certificate">
  <svg class="backdrop" width="1200" height="927" viewBox="0 0 1200 927" aria-hidden="true">
    <defs>
      <linearGradient id="navyFill" x1="0" y1="0" x2="0" y2="1">
        <stop offset="0" stop-color="#004f85"/>
        <stop offset="0.55" stop-color="#002a62"/>
        <stop offset="1" stop-color="#001d52"/>
      </linearGradient>
      <linearGradient id="goldBand" x1="0" y1="0" x2="1" y2="0">
        <stop offset="0" stop-color="#f3d060"/>
        <stop offset="0.5" stop-color="#c9932e"/>
        <stop offset="1" stop-color="#f3d060"/>
      </linearGradient>
      <linearGradient id="greyLeft" x1="0" y1="0" x2="1" y2="0">
        <stop offset="0" stop-color="#a9a9a9"/>
        <stop offset="1" stop-color="#f2f2f2"/>
      </linearGradient>
      <linearGradient id="greyRight" x1="1" y1="0" x2="0" y2="0">
        <stop offset="0" stop-color="#a9a9a9"/>
        <stop offset="1" stop-color="#f2f2f2"/>
      </linearGradient>
      <radialGradient id="sealGold" cx="0.4" cy="0.35" r="0.7">
        <stop offset="0" stop-color="#fbe38a"/>
        <stop offset="0.6" stop-color="#e0ad3f"/>
        <stop offset="1" stop-color="#b7802a"/>
      </radialGradient>
      <radialGradient id="sealNavy" cx="0.4" cy="0.3" r="0.8">
        <stop offset="0" stop-color="#2c3550"/>
        <stop offset="1" stop-color="#0d1530"/>
      </radialGradient>
    </defs>
    <polygon points="0,222 430,330 0,476" fill="url(#greyLeft)"/>
    <polygon points="1200,222 770,330 1200,482" fill="url(#greyRight)"/>
    <polygon points="0,0 1200,0 1200,190 600,352 0,180" fill="url(#navyFill)"/>
    <polygon points="0,125 600,352 0,180" fill="var(--navy-shadow)" opacity="0.55"/>
    <polygon points="1200,135 600,352 1200,190" fill="var(--navy-shadow)" opacity="0.55"/>
    <polygon points="0,180 600,345 1200,190 1200,232 600,375 0,222" fill="url(#goldBand)"/>
    <rect x="34" y="32" width="1128" height="800" fill="none" stroke="var(--gold-dark)" stroke-width="1.5" opacity="0"/>
    <polyline points="355,832 34,832 34,32 1162,32 1162,832 866,832" fill="none" stroke="var(--gold-dark)" stroke-width="1.6"/>
    <circle cx="592" cy="306" r="102" fill="url(#sealGold)"/>
    <circle cx="592" cy="306" r="84" fill="url(#sealNavy)"/>
    <circle cx="592" cy="306" r="78" fill="none" stroke="var(--gold)" stroke-width="1.5"/>
    <line x1="164" y1="526" x2="1052" y2="526" stroke="var(--ink)" stroke-width="2"/>
    <circle cx="196" cy="526" r="3.5" fill="var(--ink)"/>
    <circle cx="1020" cy="526" r="3.5" fill="var(--ink)"/>
  </svg>

  <h1 class="title">Congratulations!</h1>
  <p class="recipient">INSERT NAME?</p>
  <p class="achievement">had a successful vasectomy!</p>

  <div class="date-field">
    <span class="date-label">Date</span>
    <div class="date-line"></div>
  </div>

  <div class="brand">
    <span class="brand-square"></span>
    <span class="brand-name">Clearpath<br>Vasectomy</span>
  </div>

  <div class="signature-mark" role="img" aria-label="Handwritten signature of Dr Mark Ellison"></div>
  <div class="signatory">
    <p class="signatory-name">Dr Mark Ellison</p>
    <p class="signatory-org">Clearpath Vasectomy</p>
  </div>

  <p class="website">www.clearpathvasectomy.com</p>
  <div class="footer-band"></div>
</main>
</body>
</html>
```